We need letterhead, Business Cards, and envelops designed. We have attached a design of our logo and a sample of letterhead idea that was started but never perfected, it is only an idea for the letterhead if you can design something better we may love that also we are open to change.
We want a design that looks professional in style. we are a non profit trade association in the construction industry. the green color in the attached design represent green building, and we like that. also if you just want to enhance the letterhead sample that we attached that would be fine also.
Thanks and good luck
also the name that should show on the first business cards should be Merwin Habsfield, Director are web address is www.tqvmp.org

```html
<!DOCTYPE html>
<html lang="en">
<head>
<meta charset="utf-8">
<title>TQVMP Stationery Set</title>
<link rel="stylesheet" href="https://fonts.googleapis.com/css2?family=Arimo:wght@400&family=Open+Sans:wght@400;600&display=swap">
<style>
  :root {
    --backdrop: #d4dcf5;
    --paper: #ffffff;
    --paper-edge: #c3c8d6;
    --sheet-shadow: rgba(40, 45, 70, 0.45);
    --brand-green: #3d7a1a;
    --accent-green: #9ad66b;
    --ink: #111111;
    --ink-soft: #222222;
  }
  * { margin: 0; padding: 0; box-sizing: border-box; }
  html, body { width: 1200px; height: 1000px; overflow: hidden; }
  body { background: var(--backdrop); position: relative; font-family: "Open Sans", Arial, sans-serif; }

  .sheet {
    position: absolute;
    background: var(--paper);
    border: 1px solid var(--paper-edge);
    box-shadow: 3px 5px 8px var(--sheet-shadow);
  }
  .brand-bar { position: absolute; background: var(--brand-green); }
  .brand-name {
    position: absolute;
    font-family: "Open Sans", Arial, sans-serif;
    font-weight: 400;
    color: var(--ink);
    line-height: 1;
    display: flex;
    align-items: center;
    gap: 8px;
    letter-spacing: 1px;
    white-space: nowrap;
  }
  .brand-name .brand-square { background: var(--brand-green); display: inline-block; }

  /* Letterhead */
  .letterhead { left: 34px; top: 68px; width: 593px; height: 840px; }
  .letterhead .brand-bar { left: 27px; top: -1px; width: 137px; height: 19px; }
  .letterhead .brand-name { left: 27px; top: 30px; font-size: 34px; }
  .letterhead .brand-square { width: 12px; height: 12px; }
  .contact-col {
    position: absolute;
    top: 27px;
    border-left: 3px dotted var(--accent-green);
    padding-left: 7px;
    font-size: 10px;
    font-weight: 600;
    line-height: 13.5px;
    color: var(--ink);
    white-space: nowrap;
  }
  .contact-col.address { left: 377px; }
  .contact-col.reach { left: 461px; }

  /* Business card */
  .business-card { left: 572px; top: 284px; width: 315px; height: 204px; }
  .business-card .brand-bar { left: 17px; top: -1px; width: 124px; height: 15px; }
  .business-card .brand-name { left: 17px; top: 24px; font-size: 29px; }
  .business-card .brand-square { width: 10px; height: 10px; }
  .card-person { position: absolute; left: 22px; right: 0; top: 96px; text-align: center; font-family: "Arimo", Arial, sans-serif; white-space: nowrap; }
  .card-person .person-name { font-size: 15px; color: var(--ink-soft); line-height: 19px; }
  .card-person .person-role { font-size: 14px; color: var(--brand-green); line-height: 19px; }
  .card-web { position: absolute; left: 22px; top: 177px; font-size: 13px; color: var(--brand-green); white-space: nowrap; }

  /* Envelope */
  .envelope { left: 483px; top: 534px; width: 681px; height: 340px; }
  .envelope .brand-bar { left: 44px; top: -1px; width: 157px; height: 28px; }
  .envelope .brand-name { left: 44px; top: 36px; font-size: 38px; }
  .envelope .brand-square { width: 13px; height: 13px; }
</style>
</head>
<body>

  <section class="sheet letterhead" aria-label="Letterhead">
    <div class="brand-bar"></div>
    <div class="brand-name"><span>TQVMP</span><span class="brand-square"></span></div>
    <div class="contact-col address">
      <div>State one</div>
      <div>adddress line 1</div>
      <div>address line 2</div>
    </div>
    <div class="contact-col reach">
      <div>Phone: 555014822</div>
      <div>Fax: 555014823</div>
      <div>www.tqvmp.com</div>
    </div>
  </section>

  <section class="sheet business-card" aria-label="Business card">
    <div class="brand-bar"></div>
    <div class="brand-name"><span>TQVMP</span><span class="brand-square"></span></div>
    <div class="card-person">
      <div class="person-name">Merwin Habsfield</div>
      <div class="person-role">Director</div>
    </div>
    <div class="card-web">www.tqvmp.org</div>
  </section>

  <section class="sheet envelope" aria-label="Envelope">
    <div class="brand-bar"></div>
    <div class="brand-name"><span>TQVMP</span><span class="brand-square"></span></div>
  </section>

</body>
</html>
```